Web Design Project for Tessiloq Harbor

Need a website designed, coded and implemented on our server for a subdomain of our main web site tessiloq.com to promote commercial outdoor furniture products and a modular deck product. The requirements are hopefully explained in sufficient detail in the attached word document.

I understand at first the budget on the project is low but I'm looking to see the designs submitted first then once I have chosen a winner, I will increase the budget with what will be agreed on between me and the winning designer.

```html
<!DOCTYPE html>
<html lang="en">
<head>
<meta charset="utf-8">
<title>Tessiloq Harbor – Street Life, Town Life</title>
<link href="https://fonts.googleapis.com/css2?family=Montserrat:wght@400;500;600;700;800&display=swap" rel="stylesheet">
<style>
:root{
  --orange:#dd6a32;
  --teal:#155c66;
  --teal-dark:#1d3e48;
  --footer:#1c4b58;
  --ink:#2a2a2a;
  --grey:#666;
  --white:#fff;
  --hero-tone:#4a4f45;
  --photo-parklet:#55524b;
  --photo-cafe:#a7aaa4;
  --photo-pool:#9fb3b0;
  --photo-bench:#d9e9ed;
  --photo-planter:#4b4740;
  --photo-modular:#6d6a66;
  --photo-solar:#3a3d35;
}
*{box-sizing:border-box;margin:0;padding:0}
html,body{width:1200px;height:4484px;overflow:hidden;background:var(--white);font-family:"Montserrat",sans-serif;color:var(--ink)}
.page{position:relative;width:1200px;height:4484px}

.masthead{height:47px;display:flex;align-items:center;justify-content:center;gap:7px}
.brand-mark{width:12px;height:12px;background:var(--teal)}
.brand-name{font-size:18px;font-weight:500;color:var(--teal)}

.main-nav{height:37px;background:var(--orange);display:flex;align-items:stretch;padding-left:171px}
.main-nav a{display:flex;align-items:center;padding:0 14px;font-size:10.5px;color:var(--white);text-decoration:none;letter-spacing:.2px}
.main-nav a.is-active{background:var(--teal);padding:0 17px}

.hero{position:relative;height:511px;background:var(--hero-tone)}
.hero-title{position:absolute;top:172px;width:100%;text-align:center;font-size:62px;line-height:76px;font-weight:800;color:var(--white);letter-spacing:-.5px}
.hero-sub{position:absolute;top:262px;width:100%;text-align:center;font-size:22px;line-height:28px;font-weight:700;color:var(--white)}
.hero-dots{position:absolute;right:63px;top:226px;display:flex;flex-direction:column;gap:6px}
.hero-dots span{width:8px;height:8px;border-radius:50%;background:var(--white)}

.pillars{position:absolute;top:460px;left:164px;display:flex;z-index:2}
.pillar{width:291px;height:270px;background:var(--teal);color:var(--white);text-align:center;padding-top:50px}
.pillar.is-dark{background:var(--teal-dark)}
.pillar h2{font-size:46px;font-weight:400;letter-spacing:1px;margin-bottom:24px}
.pillar p{font-size:18px;font-weight:700;line-height:1.45;padding:0 45px}

.feature{position:absolute;left:172px;width:856px;height:383px;display:flex;justify-content:space-between;align-items:flex-start}
.feature .photo{width:421px;height:383px}
.feature .copy{width:390px;padding-top:42px}
.feature.is-reversed{flex-direction:row-reverse}
.feature.is-reversed .copy{width:380px}
.copy h3{font-size:32px;font-weight:500;line-height:1.3;text-transform:uppercase;margin-bottom:20px}
.copy ul{list-style:none;margin-bottom:28px}
.copy li,.copy p{font-size:12.5px;color:var(--grey);line-height:2}
.copy p{margin-bottom:28px}
.btn{display:inline-flex;align-items:center;justify-content:center;width:186px;height:54px;border-radius:27px;background:var(--orange);color:var(--white);font-size:16px;font-weight:700;text-decoration:none}

.site-footer{position:absolute;top:4142px;left:0;width:1200px;height:342px;background:var(--footer);color:var(--white)}
.foot-col{position:absolute;top:58px}
.foot-col a,.foot-col h4{display:block;font-size:12.5px;color:var(--white);text-decoration:none;margin-bottom:27px;font-weight:400}
.foot-col h4{color:var(--orange);font-weight:700}
.foot-about{position:absolute;left:599px;top:58px;width:460px}
.foot-about h4{font-size:12.5px;color:var(--orange);font-weight:700;margin-bottom:16px}
.foot-about p{font-size:11px;line-height:1.6}
.foot-legal{position:absolute;left:145px;top:298px;font-size:12.5px}
.social-square{position:absolute;left:1030px;top:294px;width:22px;height:22px;border-radius:3px;background:var(--white)}
</style>
</head>
<body>
<div class="page">
  <header class="masthead">
    <span class="brand-mark"></span><span class="brand-name">Tessiloq Harbor</span>
  </header>
  <nav class="main-nav">
    <a class="is-active" href="#">HOME</a>
    <a href="#">CURBDECK INTRO</a>
    <a href="#">DECK SIZE</a>
    <a href="#">DECK SURFACE</a>
    <a href="#">RAILINGS</a>
    <a href="#">PLANTERS</a>
    <a href="#">ACCESSORIES</a>
    <a href="#">CONSTRUCTION</a>
    <a href="#">MORE</a>
  </nav>

  <section class="hero" role="img" aria-label="Rooftop terrace with lounge sofas, planters and a view over green treetops">
    <h1 class="hero-title">STREET LIFE-TOWN LIFE</h1>
    <p class="hero-sub">Bringing Space, Color &amp; Light to Urban Environments</p>
    <div class="hero-dots"><span></span><span></span><span></span><span></span></div>
  </section>

  <div class="pillars">
    <div class="pillar"><h2>SPACE</h2><p>CurbDeck' kits for Parklets &amp; roadside dining</p></div>
    <div class="pillar is-dark"><h2>COLOR</h2><p>Colorful &amp; Cheerful Cafe, Street &amp; Park Furniture</p></div>
    <div class="pillar"><h2>LIGHT</h2><p>Illuminated Planters &amp; Solar Seating</p></div>
  </div>

  <section class="feature" style="top:812px">
    <div class="copy">
      <h3>'CurbDeck'<br>Parklet Kits</h3>
      <ul><li>Self-contained modular deck kits</li><li>For growing strong, integrated communities</li><li>Adaptable, customizable, extendable</li><li>Temporary of permanent</li></ul>
      <a class="btn" href="#">READ MORE</a>
    </div>
    <div class="photo" role="img" aria-label="Two people dining on a street parklet deck framed by black planters" style="background:var(--photo-parklet)"></div>
  </section>

  <section class="feature is-reversed" style="top:1289px">
    <div class="copy">
      <h3>Bright, Cheerful<br>Cafe Furniture</h3>
      <ul><li>More smiles, more fun, more enjoyment.</li><li>Durable cafe and street furniture in bright cheerful colors.</li><li>Stackable chairs, benches, tables.</li><li>Aluminum or steel.Fixed mount or loose.</li></ul>
      <a class="btn" href="#">READ MORE</a>
    </div>
    <div class="photo" role="img" aria-label="Yellow metal cafe table and chairs on a city sidewalk" style="background:var(--photo-cafe)"></div>
  </section>

  <section class="feature" style="top:1766px">
    <div class="copy">
      <h3>Porcelain Planters,<br>Tables,Chairs &amp;<br>Benches</h3>
      <p>Total coordination of paving, planters and outdoor furniture<br>Strong, durable, fade resistant, low maintenance porcelain<br>30+ color options.</p>
      <a class="btn" href="#">READ MORE</a>
    </div>
    <div class="photo" role="img" aria-label="Pool terrace with porcelain paving and square planters" style="background:var(--photo-pool)"></div>
  </section>

  <section class="feature is-reversed" style="top:2243px">
    <div class="copy">
      <h3>Bench Seating with<br>Color &amp; Style</h3>
      <ul><li>Durable bench seating in bold, bright &nbsp;colors for lively</li><li>recreation and play areas.</li><li>Powder coated steel frames</li><li>Natural wood seating</li></ul>
      <a class="btn" href="#">READ MORE</a>
    </div>
    <div class="photo" role="img" aria-label="Three wooden benches with yellow, red and grey steel frames" style="background:var(--photo-bench)"></div>
  </section>

  <section class="feature" style="top:2720px">
    <div class="copy">
      <h3>Illuminated<br>Planters</h3>
      <ul><li>PANELS</li><li>Planters with personality. Bright, light and airy.</li><li>Powder coated aluminum</li><li>Integrated LED lighting.</li></ul>
      <a class="btn" href="#">READ MORE</a>
    </div>
    <div class="photo" role="img" aria-label="White planters with glowing cut-out panels at night" style="background:var(--photo-planter)"></div>
  </section>

  <section class="feature is-reversed" style="top:3198px">
    <div class="copy">
      <h3>Modular Planters<br>&amp; Bench Seating</h3>
      <ul><li>Steel framed planters with porcelain or Ipe wood panels.</li><li>70+ porcelain color options</li><li>Extendable to any length</li><li>Integrated bench seating.</li></ul>
      <a class="btn" href="#">READ MORE</a>
    </div>
    <div class="photo" role="img" aria-label="Wooden bench between two grey planters on gravel" style="background:var(--photo-modular)"></div>
  </section>

  <section class="feature" style="top:3675px">
    <div class="copy">
      <h3>Solar Bench<br>Seating</h3>
      <p>Gather around a 'Meridian' Solar Charging Station to charge<br>your phone or respond to an email on the go. Our range of<br>solar products offers endless opportunities for<br>sustainable connection.</p>
      <a class="btn" href="#">READ MORE</a>
    </div>
    <div class="photo" role="img" aria-label="White solar bench lit up on grass at night" style="background:var(--photo-solar)"></div>
  </section>

  <footer class="site-footer">
    <div class="foot-col" style="left:145px"><a href="#">CONTACT</a><a href="#">SOLAR</a><a href="#">FURNITURE</a><a href="#">CURBDECK</a></div>
    <div class="foot-col" style="left:338px"><h4>RESOURCES</h4><a href="#">SOLAR SPEC SHEETS</a><a href="#">PARKLET RESOURCES</a><a href="#">PORCELAIN PAVERS</a></div>
    <div class="foot-about">
      <h4>ABOUT US</h4>
      <p>Tessiloq Harbor is always looking for new ways to add character and elegance to outdoor landscapes with innovative products. In addition to our primary range porcelain pavers and support pedestals, we now offer a range of urban outdoor furniture and solar products such as benches, picnic tables and path lights for safe and sustainable environments. In 2018, we pioneered 'CurbDeck' outdoor seating platforms: modular, ready-to-assemble parklets and pedlets for parks and recreation facilities, designed for both temporary and permanent applications.</p>
    </div>
    <p class="foot-legal">Tessiloq Harbor Inc. © 2021 - All Rights Reserved &nbsp;| &nbsp;Privacy Policy &nbsp;| &nbsp;Terms and Conditions</p>
    <span class="social-square"></span>
  </footer>
</div>
</body>
</html>
```